Web Design Project

I'm an author in need of a personal web site. My writing is dark and dramatic but also beautiful and artistic, and I would like the site to reflect this. Dark colours are preferred - eg grey, black.

I prefer wide-screen layouts where the images flow unbroken to the edge of the screen. I've had professional photos taken and would like to use a different photo as a header for each page (see this site as an example of the feel I'm after: www.orlavimstead.com).

I like the use of texture and layers. I want the pages to have depth. eg Distressed/ vintage effects where the edges fade to black.

Target Market(s)

Women age 20-50

Industry/Entity Type

It Professional

Requirements
Must have
• Page 1 - Home (Photo IMG_0054) (to include Quillo feed, Pagemarsh "Like" box, and form to collect subscribers to an e-newsletter)
Page 2 - About me (IMG_9862)
Page 3 - My novel (ONE SHEET pdf)
Page 4 - Journal (a blog page) (IMG_0079)
Page 5 - Press (IMG_9948)
Page 6 - Links (IMG_0119)
Page 7 - Contact (IMG_0084) (contact form for email, plus buttons for Quillo and Pagemarsh)

```html
<!DOCTYPE html>
<html lang="en">
<head>
<meta charset="utf-8">
<title>About Me · Mara Holloway</title>
<link rel="stylesheet" href="https://fonts.googleapis.com/css2?family=Sorts+Mill+Goudy:ital@0;1&family=Parisienne&family=Tangerine:wght@700&display=swap">
<style>
  :root {
    --page-black: #0e0d0c;
    --header-dark: #1b1a17;
    --header-field: #4a4536;
    --header-sky: #8a8878;
    --paper: #d9d2c7;
    --paper-light: #e2dcd2;
    --band-light: #efe6cf;
    --band-mid: #e2d5b4;
    --band-dark: #c4b28a;
    --band-edge: #9c8a64;
    --ink: #3b302a;
    --ink-soft: #5a4e45;
    --accent: #8e2414;
    --nav-ink: #3a2418;
    --white: #f3efe8;
    --divider: #7b736a;
    --footer-current: #d2703c;
  }
  * { box-sizing: border-box; margin: 0; padding: 0; }
  html, body { width: 1200px; height: 2169px; overflow: hidden; background: var(--page-black); }
  body { position: relative; font-family: "Sorts Mill Goudy", Georgia, serif; color: var(--ink); }

  .hero {
    position: absolute; left: 0; top: 0; width: 1200px; height: 610px;
    background:
      radial-gradient(ellipse 75% 65% at 55% 40%, rgba(0,0,0,0) 35%, rgba(0,0,0,.85) 100%),
      linear-gradient(180deg, var(--header-sky) 0%, #6f6d60 26%, var(--header-field) 38%, #3a3428 68%, var(--header-dark) 100%);
  }
  .hero-portrait {
    position: absolute; left: 745px; top: 205px; width: 350px; height: 360px; border-radius: 40%;
    background: radial-gradient(ellipse at 50% 45%, rgba(176,154,128,.75) 0%, rgba(110,92,74,.5) 45%, rgba(60,50,40,0) 72%);
  }
  .site-name {
    position: absolute; left: 108px; top: 66px;
    font-size: 66px; line-height: 80px; color: var(--white); letter-spacing: 1px;
  }
  .social { position: absolute; right: 48px; top: 50px; display: flex; gap: 12px; }
  .social span { display: flex; align-items: center; gap: 5px; font-size: 15px; color: var(--white); }
  .social span::before { content: ""; width: 12px; height: 12px; background: #cfcac0; }
  .hero-quote {
    position: absolute; left: 226px; top: 362px; width: 420px;
    font-family: "Parisienne", cursive; font-size: 26px; line-height: 32px; color: var(--white);
  }
  .hero-quote cite { display: block; margin: 8px 0 0 205px; font-style: normal; font-size: 21px; }

  .nav-band { position: absolute; left: 29px; top: 596px; width: 1142px; height: 62px; }
  .nav-band .band-shape { position: absolute; left: 0; top: 0; filter: drop-shadow(0 3px 4px rgba(0,0,0,.6)); }
  .nav-band a {
    position: absolute; top: 9px; font-family: "Tangerine", cursive; font-weight: 700;
    font-size: 36px; line-height: 40px; color: var(--nav-ink); text-decoration: none;
  }
  .search { position: absolute; left: 880px; top: 17px; display: flex; align-items: center; gap: 6px; }
  .search-field {
    width: 193px; height: 24px; border: 1px solid #a89a7a; background: #f1ead8;
    font-size: 13px; line-height: 16px; color: #8a7f6e; padding: 3px 6px;
  }

  .content {
    position: absolute; left: 36px; top: 656px; width: 1135px; height: 1458px;
    background: linear-gradient(180deg, var(--paper-light) 0%, var(--paper) 100%);
  }
  .divider { position: absolute; left: 849px; top: 6px; height: 1448px; border-left: 2px dashed var(--divider); }

  .story { position: absolute; left: 76px; top: 48px; width: 736px; font-size: 16.6px; line-height: 23px; }
  .story p { text-indent: 45px; margin-bottom: 27px; }
  .story .asterism { text-align: center; font-size: 30px; line-height: 24px; margin: -8px 0 26px; text-indent: 0; }

  .sidebar { position: absolute; left: 873px; top: 36px; width: 206px; }
  .sidebar blockquote { font-size: 15px; line-height: 19.5px; color: var(--ink-soft); text-align: justify; }
  .sidebar blockquote cite { display: block; text-align: right; font-style: normal; color: var(--accent); margin-top: 4px; }
  .snapshot-photo {
    margin: 62px 0 0 7px; width: 201px; height: 294px; border: 3px solid #f4efe6;
    background: linear-gradient(160deg, #b8708a 0%, #c05030 40%, #d69a62 60%, #8a4a6a 100%);
    box-shadow: 0 2px 4px rgba(0,0,0,.35);
  }
  .snapshot { margin-top: 58px; font-size: 14px; line-height: 18px; }
  .snapshot h3 { font-size: 14px; font-weight: normal; color: var(--accent); margin-bottom: 18px; }
  .snapshot dt { font-style: italic; text-decoration: underline; color: var(--ink-soft); }
  .snapshot dd { padding-left: 46px; margin-bottom: 17px; }

  .footer {
    position: absolute; left: 0; top: 2114px; width: 1200px; height: 55px; background: var(--page-black);
    font-size: 14.5px; color: var(--white);
  }
  .footer nav { position: absolute; left: 80px; top: 18px; display: flex; gap: 10px; }
  .footer a { color: var(--white); text-decoration: none; }
  .footer a.current { color: var(--footer-current); }
  .footer small { position: absolute; left: 592px; top: 21px; font-size: 11px; }
</style>
</head>
<body>
  <header class="hero" role="img" aria-label="Photograph of the author seated on a white wooden chair in a grassy field at dusk">
    <div class="hero-portrait"></div>
  </header>
  <div class="site-name">Mara Holloway</div>
  <div class="social"><span>Quillo</span><span>Pagemarsh</span></div>
  <blockquote class="hero-quote">“Ink on paper is as beautiful to me<br>as flowers on the mountains.<br>God composes; why shouldn’t we?”<cite>Tessa Galloway</cite></blockquote>

  <div class="nav-band">
    <svg class="band-shape" width="1142" height="62" viewBox="0 0 1142 62" aria-hidden="true">
      <defs>
        <linearGradient id="band-fill" x1="0" y1="0" x2="0" y2="1">
          <stop offset="0" stop-color="var(--band-mid)"/>
          <stop offset="0.35" stop-color="var(--band-light)"/>
          <stop offset="0.75" stop-color="var(--band-mid)"/>
          <stop offset="1" stop-color="var(--band-dark)"/>
        </linearGradient>
        <linearGradient id="band-age" x1="0" y1="0" x2="1" y2="0">
          <stop offset="0" stop-color="var(--band-edge)" stop-opacity=".55"/>
          <stop offset="0.08" stop-color="var(--band-edge)" stop-opacity="0"/>
          <stop offset="0.5" stop-color="var(--band-edge)" stop-opacity=".12"/>
          <stop offset="0.92" stop-color="var(--band-edge)" stop-opacity="0"/>
          <stop offset="1" stop-color="var(--band-edge)" stop-opacity=".55"/>
        </linearGradient>
      </defs>
      <path d="M4 6 L60 3 L130 7 L210 2 L300 6 L390 3 L470 8 L560 4 L650 7 L740 2 L830 6 L920 3 L1010 7 L1080 3 L1138 6 L1135 20 L1140 34 L1136 48 L1139 58 L1060 55 L980 60 L900 56 L810 60 L720 55 L630 59 L540 55 L450 60 L360 56 L270 59 L180 55 L100 60 L40 56 L2 59 L6 44 L1 30 L5 18 Z" fill="url(#band-fill)"/>
      <path d="M4 6 L60 3 L130 7 L210 2 L300 6 L390 3 L470 8 L560 4 L650 7 L740 2 L830 6 L920 3 L1010 7 L1080 3 L1138 6 L1135 20 L1140 34 L1136 48 L1139 58 L1060 55 L980 60 L900 56 L810 60 L720 55 L630 59 L540 55 L450 60 L360 56 L270 59 L180 55 L100 60 L40 56 L2 59 L6 44 L1 30 L5 18 Z" fill="url(#band-age)" stroke="var(--band-edge)" stroke-width="1"/>
    </svg>
    <nav>
      <a href="#" style="left:83px">Home</a>
      <a href="#" class="current" style="left:168px">About Me</a>
      <a href="#" style="left:320px">My Novel</a>
      <a href="#" style="left:455px">Journal</a>
      <a href="#" style="left:570px">Press</a>
      <a href="#" style="left:649px">Links</a>
      <a href="#" style="left:730px">Contact</a>
    </nav>
    <div class="search">
      <div class="search-field">search on site...</div>
      <svg width="42" height="30" viewBox="0 0 44 30" aria-hidden="true"><circle cx="26" cy="13" r="10" fill="#d6d2c8" stroke="#6d6558" stroke-width="2"/><line x1="18" y1="20" x2="6" y2="27" stroke="#6d6558" stroke-width="4" stroke-linecap="round"/></svg>
    </div>
  </div>

  <main class="content">
    <article class="story">
      <p>I knew what I wanted to do with my life at the age of six.</p>
      <p>See, I’ve always loved stories. The picture below is proof of that - it’s me as a baby, fallen fast asleep in the middle of “reading” my Little Amber Book.</p>
      <p>So perhaps it’s not surprising that I should remember this particular moment so vividly.</p>
      <p>I sat cross-legged on the carpet in my Grade One classroom, staring up with rapt attention at the Big Book splayed open on the easel. My mouth moved along with the teacher as she pointed to the letters one by one, sounding them out. And as she did, something magical happened. A type of alchemy in paper and ink. For the first time I understood the connection between the symbols on the page and the stories I loved to hear.</p>
      <p>My whole body tingled with the power of this discovery. A secret key had been pressed into my palm.</p>
      <p>I could read.</p>
      <p>In the midst of this startling revelation, a brand new question took root in my head. I mulled it over all day, then went home and asked my mother. “Where do all the storybooks come from?”</p>
      <p>“People write them,” she said. “A person who writes a book is called an author.”</p>
      <p>Her words fell with absolute clarity, like sunlight through cut glass. Imagine! People made up stories about whatever they wanted. And that was their job! This had to be the most exciting thing I’d ever heard. Right then and there, I knew.</p>
      <p>I was going to be an author.</p>
      <p class="asterism">✻</p>
      <p>God planted a seed of destiny in my heart that day, and it’s never gone away. I’ve done a lot of other things since then. I studied Education, and taught Art and Drama for several years. Travelled the world. Got married. Had babies.</p>
      <p>But all the while, I wrote. Short stories. The opening chapters of books. Eventually, a whole novel, and then another.</p>
      <p>The road to publication has not been easy. And that’s a very good thing. It’s forced me to become a better writer. To hone my craft. To develop as a person, with a deeper understanding of what makes us human - the common heart-cries that bind us together, no matter how different we may appear. And along the way, I’ve grown to understand that while God may call us to something, it’s our job to grow into that calling. To take our raw talent and shape it into something worthwhile, then offer it back to Him for His glory.</p>
      <p>So, no matter how long it takes to realize that childhood dream, I’ll keep on writing. Storytelling is in my blood.</p>
      <p>One of these days, a novel I’ve written might just sit on your shelf.</p>
    </article>

    <div class="divider"></div>

    <aside class="sidebar">
      <blockquote>“The maker of a sentence launches out into the infinite and builds a road into Chaos and old Night, and is followed by those who hear him with something of wild, creative delight.”<cite>Rowan Wade Ellery</cite></blockquote>
      <div class="snapshot-photo" role="img" aria-label="Childhood photo of the author as a baby asleep over an open picture book"></div>
      <section class="snapshot">
        <h3>Snapshot:</h3>
        <dl>
          <dt>Location:</dt><dd>Queensland, Australia</dd>
          <dt>Family:</dt><dd>Two boys, ages 3 and 1.</dd>
          <dt>What I write:</dt><dd>Inspirational Women’s fiction</dd>
          <dt>Writing style:</dt><dd>Lyrical. Compelling. Dark. Redemptive.</dd>
          <dt>Other Interests:</dt><dd>Art and Interior Design.</dd>
        </dl>
      </section>
    </aside>
  </main>

  <footer class="footer">
    <nav>
      <a href="#">Home</a><a href="#" class="current">About Me</a><a href="#">My Novel</a><a href="#">Journal</a><a href="#">Press</a><a href="#">Links</a><a href="#">Contact</a>
    </nav>
    <small>© 2011 Mara Holloway. All rights reserved.</small>
  </footer>
</body>
</html>
```